Nutrigenomics Business card design

Nutrigenomics is an exciting emerging field where I sequence the DNA from a saliva swab and then tailor a personalised nutritional program according to the persons genetics. It is possible to turn down undesirable genes that may be stuck "on" all the time causing inflammation etc. Equally important we switch "on" genes that might be stuck "off" as is often the case with autism. A large portion of my clients are autistic children. We see huge changes in functionality with the appropriate changes in diet to regulate their gene expression. This technology is definitely the way of the future.
I need a logo that will clearly show the combination of genetics with nutrition. The word "Nutrigenomics" still isn't in common use yet. I'm thinking maybe a DNA helix - (I think most people associate a helix with DNA or genes, but I'm open to suggestions) Combined somehow with food - preferably vegetables/ fruit/ meat/eggs etc. Definitely not grains or dairy - we take autistic kids off those 2 food groups straight away.
Green in it somewhere? I somehow associates healthy living / whole foods nutrition with the colour green. You guys know more about colours than me :-)
Maybe a helix could morph into a body shape filled with foods (along the lines of "you are what you eat" or something...)

Target Market(s)

The majority of my clients to date are people in their 40's wanting to improve their health or their children's health.

Industry/Entity Type

Nutrition

Contact Information for Business Card

Front of card:
Dr Moira Pellton (B App Sci, PhD Molecular Pathology)
Certified Vitacorde Practitioner and RUNE Nutritionist
52 Tallowby Rd, Tallowby
0417386254
dr.moirapellton@quillmail.com
drmoirapellton.com.au
Back of card:
Small Photo of me, Dr Moira Pellton
Specialises in Autism, ADHD, Fussy Eaters, Gut Issues, Food Intolerances, Healthy Ageing

Logo Text

Dr Moira Pellton

Logo styles of interest
Pictorial/Combination Logo
Character Logo
Requirements
Must have
• A logo showing a clear link between genes and nutrition
The box for what I want written on the card is not coming up when I try to edit so I'll put it here....
Front of card:
Dr Moira Pellton
(B App Sci, PhD Molecular Pathology) in smaller writing under my name

Certified Nutrigenomist
Certified RUNE Nutritionist

then use your nice symbols for the address, ph etc as below

52 Tallowby Rd, Tallowby
0417386254
dr.moirapellton@quillmail.com
www.drmoirapellton.com.au

Back of card:
Small Photo of me
Dr Moira Pellton
Specialises in:
Nutrigenomics
Healthy Ageing
Autism / ADHD
Gut Issues
Food Intolerances
Should not have
• No bread or grains of any sort
No dairy - milk cheese etc

```html
<!DOCTYPE html>
<html lang="en">
<head>
<meta charset="utf-8">
<title>Dr. Moira Pellton – Business Card</title>
<link rel="stylesheet" href="https://fonts.googleapis.com/css2?family=Tinos:wght@400&display=swap">
<style>
  :root {
    --card-bg: #ffffff;
    --ink: #111111;
    --green-soft: rgba(61, 181, 74, 0.16);
    --green-strong: rgba(61, 181, 74, 0.55);
    --mark-fill: #050505;
    --mark-text: #ffffff;
  }
  * { margin: 0; padding: 0; box-sizing: border-box; }
  html, body { width: 1200px; height: 693px; overflow: hidden; background: var(--card-bg); }
  .card {
    position: relative;
    width: 1200px;
    height: 693px;
    background: var(--card-bg);
    font-family: "Tinos", "Times New Roman", serif;
    color: var(--ink);
    overflow: hidden;
  }
  .backdrop {
    position: absolute;
    left: 45px;
    width: 1125px;
  }
  .backdrop--upper {
    top: 100px;
    height: 360px;
    background: radial-gradient(ellipse at 45% 40%, var(--green-soft) 0%, rgba(61, 181, 74, 0.06) 55%, rgba(61, 181, 74, 0) 75%);
  }
  .backdrop--lower {
    top: 500px;
    height: 193px;
    background: linear-gradient(to bottom, rgba(61, 181, 74, 0) 0%, var(--green-strong) 100%);
  }
  .brand-mark { position: absolute; left: 94px; top: 146px; width: 368px; height: 368px; }
  .brand-mark__name {
    font-family: "Tinos", "Times New Roman", serif;
    font-size: 40px;
    fill: var(--mark-text);
  }
  .identity { position: absolute; left: 563px; top: 172px; width: 505px; }
  .identity__name {
    font-size: 61px;
    font-weight: 400;
    line-height: 1;
    white-space: nowrap;
    letter-spacing: 0.2px;
  }
  .identity__rule { height: 3px; background: var(--ink); margin-top: 8px; }
  .identity__credentials {
    font-size: 24px;
    text-align: center;
    line-height: 1;
    margin-top: 6px;
    padding-left: 14px;
    white-space: nowrap;
  }
  .identity__rule--short { margin-left: 14px; margin-top: 5px; }
  .roles { position: absolute; left: 560px; top: 294px; }
  .roles__item { font-size: 46px; line-height: 64px; white-space: nowrap; }
  .contact { position: absolute; left: 563px; top: 430px; width: 600px; height: 70px; }
  .contact__item {
    position: absolute;
    display: flex;
    align-items: center;
    gap: 6px;
    font-size: 19.5px;
    white-space: nowrap;
  }
  .contact__icon { width: 26px; height: 26px; flex: none; }
  .contact__item--address { left: 0; top: 0; }
  .contact__item--phone { left: 0; top: 40px; }
  .contact__item--email { left: 295px; top: 0; }
  .contact__item--web { left: 295px; top: 40px; }
</style>
</head>
<body>
<main class="card">
  <div class="backdrop backdrop--upper" role="img" aria-label="Soft pale green flowing line background"></div>
  <div class="backdrop backdrop--lower" role="img" aria-label="Green flowing line band along the lower edge"></div>

  <svg class="brand-mark" viewBox="0 0 368 368" role="img" aria-label="Moira Pellton brand mark">
    <circle cx="184" cy="184" r="182" fill="var(--card-bg)" stroke="var(--mark-fill)" stroke-width="4"/>
    <circle cx="184" cy="184" r="170" fill="var(--mark-fill)"/>
    <text class="brand-mark__name" x="184" y="198" text-anchor="middle">Moira Pellton</text>
  </svg>

  <header class="identity">
    <h1 class="identity__name">Dr. Moira Pellton</h1>
    <div class="identity__rule"></div>
    <p class="identity__credentials">B App Sci, PhD Molecular Pathology</p>
    <div class="identity__rule identity__rule--short"></div>
  </header>

  <section class="roles">
    <p class="roles__item">Certified Nutrigenomist</p>
    <p class="roles__item">Certified RUNE Nutritionist</p>
  </section>

  <section class="contact">
    <p class="contact__item contact__item--address">
      <svg class="contact__icon" viewBox="0 0 26 26" aria-hidden="true">
        <circle cx="13" cy="13" r="13" fill="var(--ink)"/>
        <path d="M6 13 L13 6.5 L20 13 M8.5 11 V19.5 H17.5 V11" fill="none" stroke="#fff" stroke-width="1.8" stroke-linejoin="round"/>
      </svg>
      52 Tallowby Rd, Tallowby
    </p>
    <p class="contact__item contact__item--phone">
      <svg class="contact__icon" viewBox="0 0 26 26" aria-hidden="true">
        <circle cx="13" cy="13" r="13" fill="var(--ink)"/>
        <path d="M8.5 6.5 L11 9.5 L9.8 11.2 C10.8 13.4 12.6 15.2 14.8 16.2 L16.5 15 L19.5 17.5 L18 19.5 C12.5 19.5 6.5 13.5 6.5 8 Z" fill="#fff"/>
      </svg>
      0417386254
    </p>
    <p class="contact__item contact__item--email">
      <svg class="contact__icon" viewBox="0 0 26 26" aria-hidden="true">
        <circle cx="13" cy="13" r="13" fill="var(--ink)"/>
        <rect x="6.5" y="8.5" width="13" height="9" fill="none" stroke="#fff" stroke-width="1.4"/>
        <path d="M6.5 8.5 L13 13.5 L19.5 8.5" fill="none" stroke="#fff" stroke-width="1.4"/>
      </svg>
      dr.moirapellton@quillmail.com
    </p>
    <p class="contact__item contact__item--web">
      <svg class="contact__icon" viewBox="0 0 26 26" aria-hidden="true">
        <circle cx="13" cy="13" r="13" fill="var(--ink)"/>
        <text x="13" y="15.5" text-anchor="middle" font-size="7" fill="#fff" font-family="Tinos, serif">www</text>
      </svg>
      www.drmoirapellton.com.au
    </p>
  </section>
</main>
</body>
</html>
```